Powepoint template for an investment group

Need high end clear clean concise creative luxurious

Have royal clients
High end/billionaire investors

Using ross gold logo can be creative
Must habe page numbers
Logo preference header top right
Page number footer bottom right

The first page of the ppt maybe a big block of dark grey and ulvo investment group written on the front page in rose gold

Target Market(s)

Investors at a high level

Requirements
Must have
• Luxury feel

```html
<!DOCTYPE html>
<html lang="en">
<head>
<meta charset="utf-8">
<title>Ulvo Investment Group – Presentation Template</title>
<link rel="stylesheet" href="https://fonts.googleapis.com/css2?family=Montserrat:wght@400;500;600;700&display=swap">
<style>
:root{
  --page:#f2f2f2;
  --slide-top:#141414;
  --slide-mid:#1b1b1b;
  --slide-bottom:#383838;
  --rose:#e6a797;
  --rose-deep:#c88473;
  --rose-soft:#f0c3b6;
  --text:#d4d4d4;
  --text-dim:#a9a9a9;
  --white:#ffffff;
  --tile:#2a2a2a;
  --photo-a:#4a4f57;
  --photo-b:#8d949c;
}
*{margin:0;padding:0;box-sizing:border-box}
html,body{width:1200px;height:3914px;overflow:hidden;background:var(--page)}
body{font-family:"Montserrat",sans-serif;color:var(--text)}
.deck{display:grid;grid-template-columns:553px 553px;column-gap:31px;row-gap:29px;padding:33px}
.slide{position:relative;width:553px;height:311px;overflow:hidden;
  background:linear-gradient(180deg,var(--slide-top) 0%,var(--slide-mid) 62%,var(--slide-bottom) 100%)}
.waves{position:absolute;inset:0;width:100%;height:100%;pointer-events:none}

/* wordmark: one colour, one weight of the body font */
.wordmark{font-family:"Montserrat",sans-serif;font-weight:600;color:var(--rose);white-space:nowrap;line-height:1}
.brand{position:absolute;top:30px;right:29px;font-size:7px}
.wordmark-lg{position:absolute;left:0;right:0;text-align:center}

.slide-title{position:absolute;left:29px;font-weight:700;font-size:9px;color:var(--white);letter-spacing:.3px}
.slide-title::before{content:"";position:absolute;left:0;top:-6px;width:12px;height:1.5px;background:var(--rose)}
.slide-title.center{left:0;right:0;text-align:center}
.slide-title.center::before{left:50%;margin-left:-6px}
.copy{position:absolute;left:29px;bottom:13px;font-size:5px;color:var(--text-dim)}
.page-num{position:absolute;right:29px;bottom:13px;font-size:5px;color:var(--text-dim)}
.body{font-size:5.2px;line-height:1.55;color:var(--text)}
.body p+p{margin-top:6px}
.sub-head{font-size:5.6px;font-weight:700;color:var(--rose);margin-bottom:4px}
.item-head{font-size:5.6px;font-weight:700;color:var(--white);margin-bottom:3px}
.photo{position:absolute;background:linear-gradient(135deg,var(--photo-a),var(--photo-b))}
.abs{position:absolute}
.rose{color:var(--rose)}

.title-slide h1{position:absolute;left:0;right:0;top:153px;text-align:center;font-size:19px;font-weight:700;color:var(--white);letter-spacing:.5px}
.title-slide h1 span{color:var(--rose-soft)}
.title-slide .subtitle{position:absolute;left:0;right:0;top:184px;text-align:center;font-size:12px;color:var(--white)}
.title-slide .rule{position:absolute;left:268px;top:210px;width:18px;height:1.5px;background:var(--rose)}
.title-slide .copy{left:0;right:0;text-align:center;bottom:22px}

.boxed{position:absolute;border:1px solid #9a9a9a;border-radius:5px}
.check-list{list-style:none}
.check-list li{position:relative;padding-left:11px;margin-top:6px}
.check-list li::before{content:"";position:absolute;left:0;top:1px;width:6px;height:6px;border-radius:50%;background:var(--rose)}
.check-list li::after{content:"";position:absolute;left:1.7px;top:2.4px;width:2px;height:1.2px;border-left:1px solid #222;border-bottom:1px solid #222;transform:rotate(-45deg)}

.button{position:absolute;height:12px;background:linear-gradient(90deg,var(--rose-deep),var(--rose-soft));color:var(--white);font-size:5px;line-height:12px;padding-left:10px;border-radius:1px}
.caption{position:absolute;text-align:center;font-size:5px;line-height:1.5;color:var(--text)}

.ring-label{position:absolute;font-size:8px;font-weight:700;color:var(--white);text-align:center;width:36px;line-height:36px}

.tile{position:absolute;width:76px;height:76px;background:var(--tile);text-align:center}
.tile.active{border:1px solid var(--rose)}
.tile svg{margin-top:15px}
.tile span{display:block;font-size:7px;color:var(--white);margin-top:8px}

.card{position:absolute;width:137px;height:137px;background:#262626;text-align:center;padding:18px 16px 0}
.card .dots{margin-top:8px;letter-spacing:2px;color:var(--white);font-size:9px;line-height:1}

.data-table{position:absolute;left:207px;top:79px;width:316px;border-collapse:collapse;font-size:5px}
.data-table th{background:var(--rose-soft);color:var(--white);font-weight:500;height:24px;text-align:left;padding-left:16px}
.data-table td{height:24px;padding-left:16px;color:var(--text)}
.data-table tr:nth-child(even) td{background:#4a4444}

.stat{position:absolute;width:70px}
.stat b{display:block;font-size:12px;color:var(--white);margin-bottom:4px}
.stat-box{position:absolute;border:1px solid #9a9a9a;border-radius:4px}

.contact-list{position:absolute;left:236px;top:180px;list-style:none;font-size:6px;color:var(--white)}
.contact-list li{display:flex;align-items:center;gap:9px;height:12px}
.social{position:absolute;top:246px;width:14px;height:14px;border-radius:50%;background:var(--rose)}

.break-photo{position:absolute;inset:0;background:linear-gradient(160deg,#3a3733,#1c1b1a 55%,#2b2824)}
.break-title{position:absolute;left:29px;top:222px;font-size:23px;font-weight:700;color:var(--rose-soft)}
</style>
</head>
<body>
<main class="deck">

<!-- 1 Cover -->
<section class="slide cover">
  <div class="wordmark wordmark-lg" style="top:143px;font-size:24px">Ulvo Investment Group</div>
</section>

<!-- 2 Title -->
<section class="slide title-slide">
  <div class="wordmark wordmark-lg" style="top:100px;font-size:16px">Ulvo Investment Group</div>
  <h1>PRESENTATION <span>GOES HERE</span></h1>
  <div class="subtitle">Subtitle Presentation</div>
  <div class="rule"></div>
  <div class="copy">© 2022 Copyright ULVO Investment Group - All Rights Reserved</div>
</section>

<!-- 3 Section list -->
<section class="slide">
  <svg class="waves" viewBox="0 0 553 311"><path d="M0 250 C150 200 300 280 553 190" stroke="#2c2c2c" fill="none"/><path d="M0 270 C160 220 320 300 553 215" stroke="#262626" fill="none"/></svg>
  <div class="brand wordmark">Ulvo Investment Group</div>
  <div class="abs body" style="left:29px;top:117px;font-size:7px;color:var(--white)">Section</div>
  <div class="slide-title" style="top:131px;font-size:10px">LOREM IPSUM</div>
  <div class="abs body" style="left:29px;top:160px;width:180px">Lorem ipsum dolor sit amet, consectetuer adipiscing elit, sed diam nonummy nibh euismod tincidunt ut laoreet dolore magna aliquam erat volutpat. Ut wisi enim ad minim veniam, quis nostrud exerci tation ullamcorper suscipit lobortis nisl ut aliquip ex ea.</div>
  <div class="boxed" style="left:283px;top:122px;width:220px;height:46px"></div>
  <div class="abs body" style="left:298px;top:78px;width:190px"><div class="item-head">Lorem Ipsum</div>Lorem ipsum dolor sit amet consectetuer adipiscing elit sed diam nonummy nibh euismod tincidunt ut laoreet</div>
  <div class="abs body" style="left:298px;top:128px;width:190px"><div class="item-head">Lorem Ipsum</div>Lorem ipsum dolor sit amet consectetuer adipiscing elit sed diam nonummy nibh euismod tincidunt ut laoreet</div>
  <div class="abs body" style="left:298px;top:178px;width:190px"><div class="item-head">Lorem Ipsum</div>Lorem ipsum dolor sit amet consectetuer adipiscing elit sed diam nonummy nibh euismod tincidunt ut laoreet</div>
  <div class="abs body" style="left:298px;top:229px;width:190px"><div class="item-head">Lorem Ipsum</div>Lorem ipsum dolor sit amet consectetuer adipiscing elit sed diam nonummy nibh euismod tincidunt ut laoreet</div>
  <div class="copy">© 2022 Copyright ULVO Investment Group - All Rights Reserved</div><div class="page-num">02</div>
</section>

<!-- 4 Text + photo -->
<section class="slide">
  <div class="brand wordmark">Ulvo Investment Group</div>
  <div class="slide-title" style="top:131px">LOREM IPSUM</div>
  <div class="abs body" style="left:29px;top:148px;width:185px">Lorem ipsum dolor sit amet, consectetuer adipiscing elit, sed diam nonummy nibh euismod tincidunt ut laoreet dolore magna aliquam erat volutpat. Ut wisi enim ad minim veniam, quis nostrud exerci tation ullamcorper suscipit lobortis nisl ut aliquip ex ea</div>
  <div class="photo" role="img" aria-label="Business team meeting in a bright office" style="left:260px;top:94px;width:265px;height:148px;border-radius:6px;background:linear-gradient(135deg,#c9ccd0,#7c828a)"></div>
  <div class="copy">© 2022 Copyright ULVO Investment Group - All Rights Reserved</div><div class="page-num">02</div>
</section>

<!-- 5 Two columns -->
<section class="slide">
  <div class="brand wordmark">Ulvo Investment Group</div>
  <div class="slide-title" style="top:52px">LOREM IPSUM</div>
  <div class="abs body" style="left:29px;top:83px;width:225px"><div class="sub-head">Lorem Ipsum Dolor Sit</div>
    <p>Lorem ipsum dolor sit ametconsec adipiscing elit, sed diam nonummy nib euismod tincidunt ut laoreet mi dolorem aliquam erat volutpat. Ut wisi enim ad minim veniam, quisun nostrud exerci tati ullamcorper imn suscipit lobortis nisl ut ali ex eamnui commodo consequat. Duis autenu vel eum iriure dolor in hendrerit in vul velit esse molestie consequat, vel illum dolore eu feugiat nullam facilisis at vero eros et accumsan et iusto odio dignissi qui blandit praesent luptatum sell dei augue duis dolore te feugait nulla facil.</p>
    <p>Lorem ipsum dolor sit amet, cons ectet adipiscing elit, sed diam elim nonummy nib euismod tincidunt ut laoreet dolore magna aliquam erat piu volutpat ut wisi enim ad minim, veniam, quis nostrud exerci tati ullamcorper suscipit lobortis nisl ut ali ex ea commodo consequat orem ipsum dolor sit amet, consectetuer adipiscing elit, sed diam nonummy nibh euismod tincidunt ut laoreet dolore magna aliquam erat volutpat. Ut wisi enim ad minim.</p></div>
  <div class="abs body" style="left:296px;top:83px;width:228px"><div class="sub-head">Lorem Ipsum Dolor Sit</div>
    <p>Lorem ipsum dolor sit ametconsec adipiscing elit, sed diam nonummy nib euismod tincidunt ut laoreet mi dolorem aliquam erat volutpat. Ut wisi enim ad minim veniam, quisun nostrud exerci tati ullamcorper imn suscipit lobortis nisl ut ali ex eamnui commodo consequat. Duis autenu vel eum iriure dolor in hendrerit in vul velit esse molestie consequat, vel illum dolore eu feugiat nullam facilisis at vero eros et accumsan et iusto odio dignissi qui blandit praesent luptatum sell dei augue duis dolore te feugait nulla facil.</p>
    <p>Lorem ipsum dolor sit amet, cons ectet adipiscing elit, sed diam elim nonummy nib euismod tincidunt ut laoreet dolore magna aliquam erat piu volutpat ut wisi enim ad minim, veniam, quis nostrud exerci tati ullamcorper suscipit lobortis nisl ut ali ex ea commodo consequat orem ipsum dolor sit amet, consectetuer adipiscing elit, sed diam nonummy nibh euismod tincidunt ut laoreet dolore magna aliquam erat volutpat. Ut wisi enim ad minim.</p></div>
  <div class="copy">© 2022 Copyright ULVO Investment Group - All Rights Reserved</div><div class="page-num">02</div>
</section>

<!-- 6 Checklist + photo -->
<section class="slide">
  <div class="photo" role="img" aria-label="Hand holding a pen over a tablet at a glass desk" style="left:296px;top:0;width:257px;height:311px;background:linear-gradient(135deg,#e8ecef,#9aa4ad 60%,#5b636c)"></div>
  <div class="slide-title" style="top:52px">LOREM IPSUM</div>
  <div class="abs body" style="left:29px;top:78px;width:240px">Lorem ipsum dolor sit ametconsec adipiscing elit, sed diam nonummy nib euismod tincidunt ut laoreet mi dolorem aliquam erat volutpat. Ut wisi enim ad minim veniam, quisun nostrud exerci tati ullamcorper imn suscipit lobortis nisl ut ali ex eamnui commodo consequat. Duis autenu vel eum iriure dolor in hendrerit in vul velit esse molestie consequat, vel illum dolore eu feugiat nullam facilisis.
    <ul class="check-list" style="margin-top:8px">
      <li>Lorem ipsum dolor sit ametconsec adipiscing elit, sed diam nonummy nib euismod tincidunt ut laoreet mi dolorem aliquam</li>
      <li>Lorem ipsum dolor sit ametconsec adipiscing elit, sed diam nonummy nib euismod tincidunt ut laoreet mi dolorem aliquam</li>
      <li>Lorem ipsum dolor sit ametconsec adipiscing elit, sed diam nonummy nib euismod tincidunt ut laoreet mi dolorem aliquam</li>
      <li>Lorem ipsum dolor sit ametconsec adipiscing elit, sed diam nonummy nib euismod tincidunt ut laoreet mi dolorem aliquam</li>
    </ul></div>
  <div class="copy">© 2022 Copyright ULVO Investment Group - All Rights Reserved</div><div class="page-num">02</div>
</section>

<!-- 7 Full text -->
<section class="slide">
  <div class="brand wordmark">Ulvo Investment Group</div>
  <div class="slide-title" style="top:52px">LOREM IPSUM</div>
  <div class="abs body" style="left:29px;top:90px;width:496px">
    <p>Lorem ipsum dolor sit amet, consectetuer adipiscing elit, sed diam nonummy nibh euismod tincidunt ut laoreet dolore magna aliquam erat volutpat. Ut wisi enim ad minim veniam, quis nostrud exerci tation ullamcorper suscipit lobortis nisl ut aliquip ex ea commodo consequat. Duis autem vel eum iriure dolor in hendrerit in vulputate velit esse molestie consequat, vel illum dolore eu feugiat nulla facilisis at vero eros et accumsan et iusto odio dignissim qui blandit praesent luptatum zzril delenit augue duis dolore te feugait nulla facilisi.</p>
    <p>Lorem ipsum dolor sit amet, cons ectetuer adipiscing elit, sed diam nonummy nibh euismod tincidunt ut laoreet dolore magna aliquam erat volutpat. Ut wisi enim ad minim veniam, quis nostrud exerci tation ullamcorper suscipit lobortis nisl ut aliquip ex ea commodo consequat.</p>
    <p>Lorem ipsum dolor sit amet, consectetuer adipiscing elit, sed diam nonummy nibh euismod tincidunt ut laoreet dolore magna aliquam erat volutpat. Ut wisi enim ad minim veniam, quis nostrud exerci tation ullamcorper suscipit lobortis nisl ut aliquip ex ea commodo consequat. Duis autem vel eum iriure dolor in hendrerit in vulputate velit esse molestie consequat, vel illum dolore eu feugiat nulla facilisis at vero eros et accumsan et iusto odio dignissim qui blandit praesent luptatum zzril delenit augue duis dolore te feugait nulla facilisi.</p>
    <p>Lorem ipsum dolor sit amet, consectetuer adipiscing elit, sed diam nonummy nibh euismod tincidunt ut laoreet dolore magna aliquam erat volutpat. Ut wisi enim ad minim veniam, quis nostrud exerci tation ullamcorper suscipit lobortis nisl ut aliquip ex ea commodo consequat.</p></div>
  <div class="copy">© 2022 Copyright ULVO Investment Group - All Rights Reserved</div><div class="page-num">02</div>
</section>

<!-- 8 Photo column + gallery -->
<section class="slide">
  <div class="photo" role="img" aria-label="Business partners joining hands over a wooden table" style="left:0;top:0;width:179px;height:311px;background:linear-gradient(160deg,#4b3a2c,#2a2420 60%,#6b5748)"></div>
  <div class="brand wordmark">Ulvo Investment Group</div>
  <div class="slide-title" style="left:207px;top:78px">LOREM IPSUM</div>
  <div class="abs body" style="left:207px;top:95px;width:318px">Lorem ipsum dolor sit amet, consectetuer adipiscing elit, sed diam nonummy nibh euismod tincidunt ut laoreet dolore magna aliquam volutpat. Ut wisi enim ad minim veniam, quis nostrud exerci tation ullamcorper suscipit lobortis nisl ut aliquip ex ea commodo consequat. Duis autem vel eum iriure dolor in hendrerit in vulputate velit esse molestie consequat, vel illum dolore eu feugiat nulla facilisis at vero eros</div>
  <div class="photo" role="img" aria-label="Two businessmen in conversation" style="left:207px;top:169px;width:101px;height:91px;background:linear-gradient(135deg,#b9c2cc,#6a7480)"></div>
  <div class="photo" role="img" aria-label="Handshake over a city skyline" style="left:316px;top:169px;width:101px;height:91px;background:linear-gradient(135deg,#a9c4e0,#4e6a8f)"></div>
  <div class="photo" role="img" aria-label="Businessman reading a tablet" style="left:424px;top:169px;width:101px;height:91px;background:linear-gradient(135deg,#e6e6e6,#6f747a)"></div>
  <div class="copy" style="color:#ddd">© 2022 Copyright ULVO Investment Group - All Rights Reserved</div><div class="page-num">02</div>
</section>

<!-- 9 Text + grid -->
<section class="slide">
  <div class="brand wordmark">Ulvo Investment Group</div>
  <div class="slide-title" style="top:52px">LOREM IPSUM</div>
  <div class="abs body" style="left:29px;top:88px;width:140px">Lorem ipsum dolor sit ametconsec adipiscing elit, sed diam nonummy nib euismod tincidunt ut laoreet mi dolorem aliquam erat volutpat. Ut wisi enim ad minim veniam, quisun nostrud exerci tati ullamcorper imn suscipit lobortis nisl ut ali ex eamnui commodo consequat. Duis autenu vel eum iriure dolor in hendrerit in vul velit esse molestie consequat, vel illum dolore eu feugiat nullam facilisis at vero eros et accumsan et iusto odio dignissi qui blandit praesent luptatum sell dei augue duis dolore te feugait nulla facil.
    <p class="rose" style="margin-top:6px">Lorem ipsum dolor sit amet, cons ectet adipiscing elit, sed diam elim nonummy nib euismod tincidunt ut laoreet.</p></div>
  <div class="boxed" style="left:357px;top:148px;width:166px;height:50px"></div>
  <div class="abs body" style="left:196px;top:94px;width:140px"><div class="sub-head">Lorem Ipsum Dolor Sit</div>Lorem ipsum dolor sit amet, umi consectetuer adipiscing elit sed diam nonummy ni euismod tincidunt ut laoreet</div>
  <div class="abs body" style="left:372px;top:94px;width:140px"><div class="sub-head">Lorem Ipsum Dolor Sit</div>Lorem ipsum dolor sit amet, umi consectetuer adipiscing elit sed diam nonummy ni euismod tincidunt ut laoreet</div>
  <div class="abs body" style="left:196px;top:154px;width:140px"><div class="sub-head">Lorem Ipsum Dolor Sit</div>Lorem ipsum dolor sit amet, umi consectetuer adipiscing elit sed diam nonummy ni euismod tincidunt ut laoreet</div>
  <div class="abs body" style="left:372px;top:154px;width:140px"><div class="sub-head">Lorem Ipsum Dolor Sit</div>Lorem ipsum dolor sit amet, umi consectetuer adipiscing elit sed diam nonummy ni euismod tincidunt ut laoreet</div>
  <div class="abs body" style="left:196px;top:214px;width:140px"><div class="sub-head">Lorem Ipsum Dolor Sit</div>Lorem ipsum dolor sit amet, umi consectetuer adipiscing elit sed diam nonummy ni euismod tincidunt ut laoreet</div>
  <div class="abs body" style="left:372px;top:214px;width:140px"><div class="sub-head">Lorem Ipsum Dolor Sit</div>Lorem ipsum dolor sit amet, umi consectetuer adipiscing elit sed diam nonummy ni euismod tincidunt ut laoreet</div>
  <div class="copy">© 2022 Copyright ULVO Investment Group - All Rights Reserved</div><div class="page-num">02</div>
</section>

<!-- 10 Four cards -->
<section class="slide">
  <div class="brand wordmark">Ulvo Investment Group</div>
  <div class="slide-title center" style="top:52px">LOREM IPSUM</div>
  <div class="abs body" style="left:150px;top:72px;width:253px;text-align:center">Lorem ipsum dolor sit amet, consectetuer adipiscing elit, sed diam nonummy nibh euismod tincidunt ut laoreet dolorenum</div>
  <div class="photo" role="img" aria-label="Businessman pointing at a chart by the sea" style="left:29px;top:109px;width:114px;height:84px;background:linear-gradient(135deg,#c9d3dc,#6f8091)"></div>
  <div class="photo" role="img" aria-label="Handshake with digital network overlay" style="left:155px;top:109px;width:114px;height:84px;background:linear-gradient(135deg,#7fa0c8,#24385a)"></div>
  <div class="photo" role="img" aria-label="Woman working at a bright digital screen" style="left:281px;top:109px;width:114px;height:84px;background:linear-gradient(135deg,#e5f1f5,#8fb0bd)"></div>
  <div class="photo" role="img" aria-label="Crowd of business people against a blue skyline" style="left:407px;top:109px;width:114px;height:84px;background:linear-gradient(135deg,#6f83c4,#1a2450)"></div>
  <div class="caption" style="left:29px;top:202px;width:114px">Lorem ipsum dolor sit amet<br>consectetuer adipiscing elit, sed<br>diam nonummy nibh euismod</div>
  <div class="caption" style="left:155px;top:202px;width:114px">Lorem ipsum dolor sit amet<br>consectetuer adipiscing elit, sed<br>diam nonummy nibh euismod</div>
  <div class="caption" style="left:281px;top:202px;width:114px">Lorem ipsum dolor sit amet<br>consectetuer adipiscing elit, sed<br>diam nonummy nibh euismod</div>
  <div class="caption" style="left:407px;top:202px;width:114px">Lorem ipsum dolor sit amet<br>consectetuer adipiscing elit, sed<br>diam nonummy nibh euismod</div>
  <div class="button" style="left:44px;top:236px;width:84px">Lorem ipsum</div>
  <div class="button" style="left:170px;top:236px;width:84px">Lorem ipsum</div>
  <div class="button" style="left:296px;top:236px;width:84px">Lorem ipsum</div>
  <div class="button" style="left:422px;top:236px;width:84px">Lorem ipsum</div>
  <div class="copy">© 2022 Copyright ULVO Investment Group - All Rights Reserved</div><div class="page-num">02</div>
</section>

<!-- 11 Diamonds + timeline -->
<section class="slide">
  <div class="brand wordmark">Ulvo Investment Group</div>
  <svg class="abs" style="left:0;top:0" width="190" height="311" viewBox="0 0 190 311">
    <defs><linearGradient id="dia" x1="0" y1="0" x2="1" y2="1"><stop offset="0" stop-color="#6b6f75"/><stop offset="1" stop-color="#a8adb3"/></linearGradient></defs>
    <polygon points="0,50 36,86 0,122" fill="var(--rose)"/>
    <polygon points="0,140 40,180 0,220" fill="var(--rose-soft)"/>
    <polygon points="0,210 36,246 0,282" fill="var(--rose-deep)"/>
    <polygon points="103,38 145,80 103,122 61,80" fill="url(#dia)" stroke="#1b1b1b" stroke-width="2"/>
    <polygon points="60,95 102,137 60,179 18,137" fill="url(#dia)" stroke="#1b1b1b" stroke-width="2"/>
    <polygon points="130,130 172,172 130,214 88,172" fill="url(#dia)" stroke="#1b1b1b" stroke-width="2"/>
    <polygon points="80,186 122,228 80,270 38,228" fill="url(#dia)" stroke="#1b1b1b" stroke-width="2"/>
  </svg>
  <div class="abs" role="img" aria-label="Four portrait photos of team members set in diamond frames" style="left:18px;top:38px;width:154px;height:232px"></div>
  <svg class="waves" viewBox="0 0 553 311"><path d="M150 100 C260 110 380 110 553 90" stroke="#333" fill="none"/><path d="M170 180 C280 175 400 175 553 160" stroke="#333" fill="none"/></svg>
  <div class="slide-title" style="left:298px;top:52px">LOREM IPSUM</div>
  <div class="abs body" style="left:331px;top:83px;width:110px"><div class="item-head">Lorem Ipsum Dolor</div>Lorem ipsum dolor sit amet, consectetuer adipiscing elit.</div>
  <div class="abs body" style="left:452px;top:135px;width:100px"><div class="item-head">Lorem Ipsum Dolor</div>Lorem ipsum dolor sit amet, consectetuer adipiscing elit.</div>
  <div class="abs body" style="left:331px;top:185px;width:110px"><div class="item-head">Lorem Ipsum Dolor</div>Lorem ipsum dolor sit amet, consectetuer adipiscing elit.</div>
  <div class="abs body" style="left:452px;top:237px;width:100px"><div class="item-head">Lorem Ipsum Dolor</div>Lorem ipsum dolor sit amet, consectetuer adipiscing elit.</div>
  <svg class="abs" style="left:260px;top:80px" width="200" height="170" viewBox="0 0 200 170">
    <g fill="var(--rose)"><circle cx="56" cy="11" r="1.5"/><circle cx="176" cy="62" r="1.5"/><circle cx="56" cy="113" r="1.5"/><circle cx="176" cy="164" r="1.5"/></g>
  </svg>
  <div class="copy">© 2022 Copyright ULVO Investment Group - All Rights Reserved</div><div class="page-num">02</div>
</section>

<!-- 12 Rings + map -->
<section class="slide">
  <div class="brand wordmark">Ulvo Investment Group</div>
  <div class="slide-title" style="top:52px">LOREM IPSUM</div>
  <svg class="abs" style="left:34px;top:104px" width="36" height="156" viewBox="0 0 36 156">
    <g fill="none" stroke-width="4">
      <circle cx="18" cy="18" r="15" stroke="#3c3c3c"/><circle cx="18" cy="18" r="15" stroke="var(--rose)" stroke-dasharray="28 94" transform="rotate(-90 18 18)"/>
      <circle cx="18" cy="69" r="15" stroke="#3c3c3c"/><circle cx="18" cy="69" r="15" stroke="var(--rose)" stroke-dasharray="47 94" transform="rotate(-90 18 69)"/>
      <circle cx="18" cy="120" r="15" stroke="#3c3c3c"/><circle cx="18" cy="120" r="15" stroke="var(--rose)" stroke-dasharray="75 94" transform="rotate(-90 18 120)"/>
    </g>
  </svg>
  <div class="ring-label" style="left:34px;top:104px">30%</div>
  <div class="ring-label" style="left:34px;top:155px">50%</div>
  <div class="ring-label" style="left:34px;top:206px">80%</div>
  <div class="abs body" style="left:84px;top:114px;width:100px">Lorem ipsum dolor sit amet, consectetuer adipiscing</div>
  <div class="abs body" style="left:84px;top:165px;width:100px">Lorem ipsum dolor sit amet, consectetuer adipiscing</div>
  <div class="abs body" style="left:84px;top:216px;width:100px">Lorem ipsum dolor sit amet, consectetuer adipiscing</div>
  <div class="abs" role="img" aria-label="World map with highlighted regions in rose gold" style="left:222px;top:106px;width:310px;height:150px;border-radius:40px;background:radial-gradient(ellipse at 50% 45%,#d8d8d8 0%,#b9b9b9 45%,rgba(185,185,185,0) 72%)"></div>
  <div class="copy">© 2022 Copyright ULVO Investment Group - All Rights Reserved</div><div class="page-num">02</div>
</section>

<!-- 13 Circle hub -->
<section class="slide">
  <div class="brand wordmark">Ulvo Investment Group</div>
  <div class="slide-title" style="top:52px">LOREM IPSUM</div>
  <div class="abs" role="img" aria-label="Silhouettes of a business team against a sunset city" style="left:210px;top:105px;width:136px;height:136px;border-radius:50%;background:radial-gradient(circle at 50% 55%,#f1b36d,#8a5a3c 55%,#2b2523)"></div>
  <svg class="abs" style="left:190px;top:85px" width="176" height="176" viewBox="0 0 176 176">
    <circle cx="88" cy="88" r="76" fill="none" stroke="#555" stroke-width="0.8"/>
    <g fill="var(--rose)" stroke="#1b1b1b" stroke-width="1.5">
      <circle cx="50" cy="22" r="11"/><circle cx="126" cy="22" r="11"/>
      <circle cx="14" cy="88" r="11"/><circle cx="162" cy="88" r="11"/>
      <circle cx="50" cy="154" r="11"/><circle cx="126" cy="154" r="11"/>
    </g>
    <g fill="none" stroke="#fff" stroke-width="1">
      <rect x="45" y="18" width="10" height="8"/><path d="M121 22h10M126 17v10"/>
      <circle cx="14" cy="88" r="4"/><path d="M157 92l5-8 5 8z"/>
      <path d="M45 154h10M50 149l5 5-5 5"/><circle cx="126" cy="154" r="4"/>
    </g>
  </svg>
  <div class="abs body" style="left:93px;top:117px;width:120px;text-align:right"><div class="item-head">Lorem ipsum</div>Lorem ipsum dolor sit ametum<br>consectetuer adipiscing elit</div>
  <div class="abs body" style="left:93px;top:163px;width:120px;text-align:right"><div class="item-head">Lorem ipsum</div>Lorem ipsum dolor sit ametum<br>consectetuer adipiscing elit</div>
  <div class="abs body" style="left:93px;top:209px;width:120px;text-align:right"><div class="item-head">Lorem ipsum</div>Lorem ipsum dolor sit ametum<br>consectetuer adipiscing elit</div>
  <div class="abs body" style="left:374px;top:117px;width:120px"><div class="item-head">Lorem ipsum</div>Lorem ipsum dolor sit ametum<br>consectetuer adipiscing elit</div>
  <div class="abs body" style="left:374px;top:163px;width:120px"><div class="item-head">Lorem ipsum</div>Lorem ipsum dolor sit ametum<br>consectetuer adipiscing elit</div>
  <div class="abs body" style="left:374px;top:209px;width:120px"><div class="item-head">Lorem ipsum</div>Lorem ipsum dolor sit ametum<br>consectetuer adipiscing elit</div>
  <div class="copy">© 2022 Copyright ULVO Investment Group - All Rights Reserved</div><div class="page-num">02</div>
</section>

<!-- 14 Icon tiles -->
<section class="slide">
  <div class="brand wordmark">Ulvo Investment Group</div>
  <div class="slide-title" style="top:52px">LOREM IPSUM</div>
  <div class="tile" style="left:116px;top:87px"><svg width="24" height="24" viewBox="0 0 24 24" fill="none" stroke="var(--rose)"><path d="M4 18c4 0 6-2 9-2h6M12 4c3 2 3 6 0 8-3-2-3-6 0-8z"/></svg><span>Lorem ipsum</span></div>
  <div class="tile active" style="left:202px;top:87px"><svg width="24" height="24" viewBox="0 0 24 24" fill="none" stroke="var(--rose)"><rect x="3" y="7" width="18" height="13" rx="2"/><circle cx="12" cy="13" r="4"/><path d="M8 7l2-3h4l2 3"/></svg><span>Lorem ipsum</span></div>
  <div class="tile" style="left:288px;top:87px"><svg width="24" height="24" viewBox="0 0 24 24" fill="none" stroke="var(--rose)"><circle cx="12" cy="12" r="9"/><path d="M15 9l-2 5-4 1 2-5z"/></svg><span>Lorem ipsum</span></div>
  <div class="tile" style="left:375px;top:87px"><svg width="24" height="24" viewBox="0 0 24 24" fill="none" stroke="var(--rose)"><path d="M2 19l7-10 4 6 3-4 6 8z"/></svg><span>Lorem ipsum</span></div>
  <div class="tile" style="left:116px;top:173px"><svg width="24" height="24" viewBox="0 0 24 24" fill="none" stroke="var(--rose)"><rect x="4" y="4" width="16" height="16"/><path d="M4 16l5-5 5 5 3-3 3 3"/></svg><span>Lorem ipsum</span></div>
  <div class="tile" style="left:202px;top:173px"><svg width="24" height="24" viewBox="0 0 24 24" fill="none" stroke="var(--rose)"><circle cx="8" cy="9" r="3"/><circle cx="16" cy="9" r="3"/><path d="M2 19c1-4 11-4 12 0M10 19c1-4 11-4 12 0"/></svg><span>Lorem ipsum</span></div>
  <div class="tile" style="left:288px;top:173px"><svg width="24" height="24" viewBox="0 0 24 24" fill="none" stroke="var(--rose)"><rect x="5" y="7" width="14" height="13" rx="2"/><path d="M9 7V4h6v3M9 11v6M15 11v6"/></svg><span>Lorem ipsum</span></div>
  <div class="tile" style="left:375px;top:173px"><svg width="24" height="24" viewBox="0 0 24 24" fill="none" stroke="var(--rose)"><path d="M5 5h14l-7 8zM12 13v7M8 20h8"/></svg><span>Lorem ipsum</span></div>
  <div class="copy">© 2022 Copyright ULVO Investment Group - All Rights Reserved</div><div class="page-num">02</div>
</section>

<!-- 15 Break -->
<section class="slide">
  <div class="break-photo" role="img" aria-label="Dim coworking office with people working at laptops"></div>
  <div class="abs wordmark" style="left:29px;top:198px;font-size:10px">Ulvo Investment Group</div>
  <div class="break-title">BREAK SLIDE</div>
  <div class="copy" style="color:#ddd">© 2022 Copyright ULVO Investment Group - All Rights Reserved</div><div class="page-num" style="color:#ddd">02</div>
</section>

<!-- 16 Band + cards -->
<section class="slide">
  <div class="photo" role="img" aria-label="Handshake in front of a city skyline" style="left:0;top:0;width:553px;height:130px;background:linear-gradient(180deg,#7d8896,#3c434c 70%,#1b1b1b)"></div>
  <div class="brand wordmark">Ulvo Investment Group</div>
  <div class="abs" style="left:0;right:0;top:70px;text-align:center;font-size:13px;font-weight:700;color:var(--white)">LOREM <span class="rose">IPSUM</span></div>
  <div class="card" style="left:74px;top:125px"><svg width="22" height="22" viewBox="0 0 22 22"><circle cx="11" cy="11" r="10" fill="var(--rose)"/><circle cx="10" cy="10" r="4" fill="none" stroke="#fff"/><path d="M13 13l3 3" stroke="#fff"/></svg><div class="body" style="margin-top:6px">Lorem ipsum dolor sit amet, consectetuer adipiscing elit, sed diam nonummy nibh eui tincidunt ut laoreet dolore magna aliquam volutpat. Ut wisi enim ad</div><div class="dots">•••</div></div>
  <div class="card" style="left:219px;top:125px"><svg width="22" height="22" viewBox="0 0 22 22"><circle cx="11" cy="11" r="10" fill="var(--rose)"/><rect x="6" y="7" width="10" height="8" fill="none" stroke="#fff"/></svg><div class="body" style="margin-top:6px">Lorem ipsum dolor sit amet, consectetuer adipiscing elit, sed diam nonummy nibh eui tincidunt ut laoreet dolore magna aliquam volutpat. Ut wisi enim ad</div><div class="dots">•••</div></div>
  <div class="card" style="left:363px;top:125px"><svg width="22" height="22" viewBox="0 0 22 22"><circle cx="11" cy="11" r="10" fill="var(--rose)"/><path d="M7 15l8-8M9 7h6v6" fill="none" stroke="#fff"/></svg><div class="body" style="margin-top:6px">Lorem ipsum dolor sit amet, consectetuer adipiscing elit, sed diam nonummy nibh eui tincidunt ut laoreet dolore magna aliquam volutpat. Ut wisi enim ad</div><div class="dots">•••</div></div>
  <div class="copy">© 2022 Copyright ULVO Investment Group - All Rights Reserved</div><div class="page-num">02</div>
</section>

<!-- 17 Hexagon process -->
<section class="slide">
  <div class="brand wordmark">Ulvo Investment Group</div>
  <div class="slide-title" style="top:52px">LOREM IPSUM</div>
  <svg class="abs" style="left:0;top:0" width="553" height="311" viewBox="0 0 553 311">
    <g stroke="#bbb" stroke-width="0.7">
      <line x1="181" y1="184" x2="181" y2="240"/><line x1="231" y1="161" x2="231" y2="210"/>
      <line x1="283" y1="184" x2="283" y2="240"/><line x1="333" y1="161" x2="333" y2="210"/>
      <line x1="384" y1="184" x2="384" y2="240"/><line x1="435" y1="161" x2="435" y2="210"/>
    </g>
    <g>
      <polygon points="231,113 252,125 252,149 231,161 210,149 210,125" fill="#3a3a3a"/>
      <polygon points="333,113 354,125 354,149 333,161 312,149 312,125" fill="#3a3a3a"/>
      <polygon points="435,113 456,125 456,149 435,161 414,149 414,125" fill="#3a3a3a"/>
      <polygon points="181,132 204,145 204,171 181,184 158,171 158,145" fill="var(--rose)"/>
      <polygon points="283,132 306,145 306,171 283,184 260,171 260,145" fill="var(--rose)"/>
      <polygon points="384,132 407,145 407,171 384,184 361,171 361,145" fill="var(--rose)"/>
    </g>
    <g fill="none" stroke="#fff" stroke-width="1">
      <rect x="178" y="150" width="6" height="10" rx="3"/><path d="M175 158c0 6 12 6 12 0M181 164v4"/>
      <rect x="224" y="132" width="14" height="9"/><path d="M227 136h8"/>
      <circle cx="278" cy="158" r="2.5"/><circle cx="288" cy="152" r="2.5"/><circle cx="288" cy="164" r="2.5"/><path d="M280 157l6-4M280 159l6 4"/>
      <circle cx="333" cy="137" r="7"/><path d="M326 137h14M333 130c-4 4-4 10 0 14M333 130c4 4 4 10 0 14"/>
      <path d="M384 149l7 3v5c0 5-7 8-7 8s-7-3-7-8v-5z"/><path d="M381 157l2 2 4-4"/>
      <path d="M429 141a4 4 0 0 1 4-7a5 5 0 0 1 9 2a3 3 0 0 1 0 5z M435 139v7"/>
    </g>
  </svg>
  <div class="caption" style="left:141px;top:243px;width:80px">Lorem ipsum dolor<br>sit amet</div>
  <div class="caption" style="left:191px;top:213px;width:80px">Lorem ipsum dolor<br>sit amet</div>
  <div class="caption" style="left:243px;top:243px;width:80px">Lorem ipsum dolor<br>sit amet</div>
  <div class="caption" style="left:293px;top:213px;width:80px">Lorem ipsum dolor<br>sit amet</div>
  <div class="caption" style="left:344px;top:243px;width:80px">Lorem ipsum dolor<br>sit amet</div>
  <div class="caption" style="left:395px;top:213px;width:80px">Lorem ipsum dolor<br>sit amet</div>
  <div class="copy">© 2022 Copyright ULVO Investment Group - All Rights Reserved</div><div class="page-num">02</div>
</section>

<!-- 18 Map features -->
<section class="slide">
  <div class="abs" role="img" aria-label="Faint world map in the background" style="left:80px;top:60px;width:400px;height:200px;background:radial-gradient(ellipse,#2a2a2a,rgba(42,42,42,0) 70%)"></div>
  <div class="abs" style="left:0;top:155px;width:553px;height:12px;background:#2c2f36"></div>
  <div class="brand wordmark">Ulvo Investment Group</div>
  <div class="slide-title" style="top:52px">LOREM IPSUM</div>
  <svg class="abs" style="left:0;top:0" width="553" height="311" viewBox="0 0 553 311">
    <g fill="#1b1b1b" stroke="var(--rose)" stroke-width="3">
      <circle cx="70" cy="138" r="12"/><circle cx="225" cy="138" r="12"/><circle cx="383" cy="138" r="12"/>
      <circle cx="146" cy="200" r="12"/><circle cx="304" cy="200" r="12"/>
    </g>
    <g fill="none" stroke="#fff" stroke-width="0.9">
      <circle cx="70" cy="138" r="4"/><path d="M70 131v3M70 142v3M63 138h3M74 138h3"/>
      <circle cx="225" cy="135" r="3"/><path d="M219 144c1-4 11-4 12 0"/>
      <rect x="378" y="133" width="10" height="10"/><path d="M381 140v-3M383 140v-5M385 140v-2"/>
      <path d="M144 196v8M148 194v8M144 204a2 2 0 1 1-2-2M148 202a2 2 0 1 1-2-2"/>
      <circle cx="304" cy="200" r="5"/><path d="M304 197v3l2 2"/>
    </g>
  </svg>
  <div class="abs body" style="left:88px;top:127px;width:105px"><div class="item-head">Lorem ipsum</div>Lorem ipsum dolor sit ametum consectetuer adipiscing elit sedu diam</div>
  <div class="abs body" style="left:243px;top:127px;width:105px"><div class="item-head">Lorem ipsum</div>Lorem ipsum dolor sit ametum consectetuer adipiscing elit sedu diam</div>
  <div class="abs body" style="left:401px;top:127px;width:105px"><div class="item-head">Lorem ipsum</div>Lorem ipsum dolor sit ametum consectetuer adipiscing elit sedu diam</div>
  <div class="abs body" style="left:164px;top:189px;width:105px"><div class="item-head">Lorem ipsum</div>Lorem ipsum dolor sit ametum consectetuer adipiscing elit sedu diam</div>
  <div class="abs body" style="left:322px;top:189px;width:105px"><div class="item-head">Lorem ipsum</div>Lorem ipsum dolor sit ametum consectetuer adipiscing elit sedu diam</div>
  <div class="copy">© 2022 Copyright ULVO Investment Group - All Rights Reserved</div><div class="page-num">02</div>
</section>

<!-- 19 Table -->
<section class="slide">
  <div class="brand wordmark">Ulvo Investment Group</div>
  <div class="slide-title" style="top:88px">LOREM IPSUM</div>
  <div class="abs body" style="left:29px;top:104px;width:142px">Lorem ipsum dolor sit amet, consectetuer adipiscing elit, sed diam nonummy nibh euismod tincidunt ut laoreet dolore magna aliquam erat volutpat. Ut wisi enim ad minim veniam, quis nostrud exerci tation ullamcorper suscipit lobortis nisl ut aliquip ex ea commodo consequat. Duis autem vel eum iriure dolor in hendrerit in</div>
  <table class="data-table">
    <tr><th>Lorem ipsum</th><th>Column 1</th><th>Column 2</th><th>Column 3</th></tr>
    <tr><td>Lorem ipsum</td><td>Lorem ipsum</td><td>Lorem ipsum</td><td>Lorem ipsum</td></tr>
    <tr><td>Lorem ipsum</td><td>Lorem ipsum</td><td>Lorem ipsum</td><td>Lorem ipsum</td></tr>
    <tr><td>Lorem ipsum</td><td>Lorem ipsum</td><td>Lorem ipsum</td><td>Lorem ipsum</td></tr>
    <tr><td>Lorem ipsum</td><td>Lorem ipsum</td><td>Lorem ipsum</td><td>Lorem ipsum</td></tr>
    <tr><td>Lorem ipsum</td><td>Lorem ipsum</td><td>Lorem ipsum</td><td>Lorem ipsum</td></tr>
    <tr><td>Lorem ipsum</td><td>Lorem ipsum</td><td>Lorem ipsum</td><td>Lorem ipsum</td></tr>
  </table>
  <div class="copy">© 2022 Copyright ULVO Investment Group - All Rights Reserved</div><div class="page-num">02</div>
</section>

<!-- 20 Stats + bar chart -->
<section class="slide">
  <div class="brand wordmark">Ulvo Investment Group</div>
  <div class="slide-title" style="top:90px">LOREM IPSUM</div>
  <div class="abs body" style="left:29px;top:106px;width:225px">Lorem ipsum dolor sit amet, consectetuer adipiscing elit, sed diam nonummy nibh euismod tincidunt ut laoreet dolore magna aliquam erat volutpat. Ut wisi enim ad minim veniam, quis nostrud exerci tation ullamcorper.</div>
  <div class="stat-box" style="left:177px;top:176px;width:81px;height:58px"></div>
  <div class="stat body" style="left:29px;top:184px"><b>3.5M</b>Lorem ipsum dolor sit amet, consectetuer adipiscing elit, sed di nonummy nibhum e</div>
  <div class="stat body" style="left:107px;top:184px"><b>5.6M</b>Lorem ipsum dolor sit amet, consectetuer adipiscing elit, sed di nonummy nibhum e</div>
  <div class="stat body" style="left:186px;top:184px"><b>6.8M</b>Lorem ipsum dolor sit amet, consectetuer adipiscing elit, sed di nonummy nibhum e</div>
  <svg class="abs" style="left:300px;top:78px" width="240" height="190" viewBox="0 0 240 190" font-family="Montserrat, sans-serif" font-size="4.5" fill="#bbb">
    <g stroke="#333" stroke-width="0.5">
      <line x1="28" y1="5" x2="240" y2="5"/><line x1="28" y1="21" x2="240" y2="21"/><line x1="28" y1="37" x2="240" y2="37"/><line x1="28" y1="53" x2="240" y2="53"/><line x1="28" y1="69" x2="240" y2="69"/><line x1="28" y1="85" x2="240" y2="85"/><line x1="28" y1="101" x2="240" y2="101"/><line x1="28" y1="117" x2="240" y2="117"/><line x1="28" y1="133" x2="240" y2="133"/><line x1="28" y1="149" x2="240" y2="149"/><line x1="28" y1="165" x2="240" y2="165"/>
    </g>
    <text x="10" y="7">100%</text><text x="12" y="23">90%</text><text x="12" y="39">80%</text><text x="12" y="55">70%</text><text x="12" y="71">60%</text><text x="12" y="87">50%</text><text x="12" y="103">40%</text><text x="12" y="119">30%</text><text x="12" y="135">20%</text><text x="12" y="151">10%</text><text x="14" y="167">0%</text>
    <g fill="var(--rose)">
      <rect x="38" y="79" width="8" height="86"/><rect x="49" y="61" width="8" height="104"/><rect x="60" y="72" width="8" height="93"/>
      <rect x="88" y="50" width="8" height="115"/><rect x="99" y="92" width="8" height="73"/><rect x="110" y="69" width="8" height="96"/>
      <rect x="138" y="65" width="8" height="100"/><rect x="149" y="52" width="8" height="113"/><rect x="160" y="80" width="8" height="85"/>
      <rect x="188" y="58" width="8" height="107"/><rect x="199" y="74" width="8" height="91"/><rect x="210" y="39" width="8" height="126"/>
    </g>
    <text x="42" y="178">Lorem ipsum</text><text x="92" y="178">Lorem ipsum</text><text x="142" y="178">Lorem ipsum</text><text x="192" y="178">Lorem ipsum</text>
  </svg>
  <div class="copy">© 2022 Copyright ULVO Investment Group - All Rights Reserved</div><div class="page-num">02</div>
</section>

<!-- 21 Icon set -->
<section class="slide">
  <div class="brand wordmark">Ulvo Investment Group</div>
  <div class="slide-title" style="top:55px">LOREM IPSUM</div>
  <svg class="abs" style="left:29px;top:74px" width="496" height="198" viewBox="0 0 496 198">
    <defs>
      <pattern id="icon-grid" width="96" height="22" patternUnits="userSpaceOnUse">
        <g fill="none" stroke="var(--rose)" stroke-width="0.9">
          <circle cx="6" cy="8" r="5"/>
          <rect x="20" y="3" width="10" height="10" rx="1"/>
          <path d="M38 13l6-10 6 10z"/>
          <path d="M58 8h10M63 3v10"/>
          <rect x="76" y="4" width="12" height="8"/><path d="M76 4l6 5 6-5"/>
        </g>
      </pattern>
      <pattern id="icon-grid-b" width="96" height="22" patternUnits="userSpaceOnUse">
        <g fill="none" stroke="var(--white)" stroke-width="0.9">
          <path d="M1 13V6l5-3 5 3v7z"/>
          <circle cx="25" cy="8" r="5"/><path d="M25 5v3l2 2"/>
          <path d="M40 3v10M44 6v7M48 9v4"/>
          <path d="M58 11c0-5 10-5 10 0zM63 11v3"/>
          <path d="M77 8l4 4 7-8"/>
        </g>
      </pattern>
    </defs>
    <rect width="496" height="198" fill="url(#icon-grid)"/>
    <rect x="48" y="11" width="448" height="187" fill="url(#icon-grid-b)" opacity=".85"/>
  </svg>
  <div class="copy">© 2022 Copyright ULVO Investment Group - All Rights Reserved</div><div class="page-num">02</div>
</section>

<!-- 22 Contact -->
<section class="slide">
  <svg class="waves" viewBox="0 0 553 311"><path d="M0 240 C150 190 330 270 553 180" stroke="#2c2c2c" fill="none"/><path d="M0 262 C170 210 340 290 553 205" stroke="#262626" fill="none"/></svg>
  <div class="wordmark wordmark-lg" style="top:115px;font-size:16px">Ulvo Investment Group</div>
  <div class="abs" style="left:0;right:0;top:150px;text-align:center;font-size:15px;font-weight:700;color:var(--white)">CONTACT US</div>
  <ul class="contact-list">
    <li><svg width="8" height="8" viewBox="0 0 8 8" fill="none" stroke="var(--rose)" stroke-width=".8"><rect x=".5" y="1.5" width="7" height="5"/><path d="M.5 1.5l3.5 3 3.5-3"/></svg>Lorem Ipsum Dolor Sit Amet</li>
    <li><svg width="8" height="8" viewBox="0 0 8 8" fill="none" stroke="var(--rose)" stroke-width=".8"><path d="M1.5 1h1.5l.7 1.8-1 .7c.5 1 1 1.5 2 2l.7-1 1.8.7V7c-3.5 0-6-2.5-6-6z"/></svg>Lorem Ipsum Dolor Sit Amet</li>
    <li><svg width="8" height="8" viewBox="0 0 8 8" fill="none" stroke="var(--rose)" stroke-width=".8"><circle cx="4" cy="4" r="3.4"/><path d="M.6 4h6.8M4 .6c-2 2-2 4.8 0 6.8M4 .6c2 2 2 4.8 0 6.8"/></svg>Lorem Ipsum Dolor Sit Amet</li>
    <li><svg width="8" height="8" viewBox="0 0 8 8" fill="none" stroke="var(--rose)" stroke-width=".8"><path d="M4 7.5S1.5 5 1.5 3a2.5 2.5 0 0 1 5 0C6.5 5 4 7.5 4 7.5z"/><circle cx="4" cy="3" r=".9"/></svg>Lorem Ipsum Dolor Sit Amet</li>
  </ul>
  <div class="social" style="left:252px"></div>
  <div class="social" style="left:270px"></div>
  <div class="social" style="left:288px"></div>
  <div class="copy">© 2022 Copyright ULVO Investment Group - All Rights Reserved</div><div class="page-num">02</div>
</section>

</main>
</body>
</html>
```